Stonegate Towing Business Card

Towing
Accident towing
Mechanical breakdown
Insurance, salvage and recovery
4wd off road towing
Light & Heavy towing
7354 2618
24 hour business 7 days

Logo can be whole size on front

Industry/Entity Type

Towing/ transport

Contact Information for Business Card

The above

```html
<!DOCTYPE html>
<html lang="en">
<head>
<meta charset="utf-8">
<title>Stonegate Towing Business Card</title>
<link href="https://fonts.googleapis.com/css2?family=Montserrat:wght@400;500;700;800&display=swap" rel="stylesheet">
<style>
  :root {
    --bg: #c4c5c8;
    --ink: #0b0b0b;
    --red: #d3202a;
    --paper: #ffffff;
    --grey: #444444;
    --white: #ffffff;
  }
  * { box-sizing: border-box; margin: 0; padding: 0; }
  html, body { width: 1200px; height: 939px; overflow: hidden; }
  body {
    background: var(--bg);
    font-family: "Montserrat", sans-serif;
    position: relative;
  }
  .card {
    position: absolute;
    width: 560px;
    height: 320px;
    border-bottom: 4px solid var(--red);
    border-right: 2px solid var(--red);
    box-shadow: 0 8px 18px rgba(0,0,0,0.22);
  }
  .card-front {
    left: 70px; top: 90px;
    background: var(--ink);
    color: var(--white);
  }
  .card-back {
    left: 570px; top: 500px;
    background: var(--paper);
    color: var(--grey);
  }
  .wordmark {
    display: flex;
    align-items: center;
    gap: 10px;
    color: var(--red);
    font-weight: 800;
  }
  .wordmark-dot {
    width: 18px; height: 18px;
    border-radius: 50%;
    background: var(--red);
    flex: none;
  }
  .card-front .wordmark {
    position: absolute;
    left: 0; right: 0; top: 92px;
    justify-content: center;
    font-size: 46px;
    letter-spacing: 0.5px;
  }
  .services {
    position: absolute;
    left: 0; right: 0; bottom: 46px;
    text-align: center;
    font-size: 13.5px;
    font-weight: 500;
    line-height: 1.75;
  }
  .services .sep { color: var(--red); padding: 0 5px; }
  .card-back .wordmark {
    position: absolute;
    left: 36px; top: 110px;
    font-size: 26px;
  }
  .card-back .wordmark-dot { width: 12px; height: 12px; }
  .person {
    position: absolute;
    left: 300px; top: 40px;
  }
  .person-name {
    color: var(--red);
    font-weight: 800;
    font-size: 22px;
  }
  .person-role {
    font-size: 13px;
    letter-spacing: 1px;
    margin-top: 4px;
    padding-left: 12px;
  }
  .service-badge {
    position: absolute;
    left: 60px; top: 200px;
    width: 90px; height: 90px;
    border-radius: 50%;
    background: var(--red);
  }
  .contacts {
    position: absolute;
    left: 300px; top: 216px;
    list-style: none;
    font-size: 13px;
    letter-spacing: 0.4px;
    color: var(--grey);
  }
  .contacts li {
    display: flex;
    align-items: center;
    gap: 8px;
    height: 22px;
  }
  .contacts svg { width: 12px; height: 12px; fill: var(--red); flex: none; }
</style>
</head>
<body>

<section class="card card-front">
  <div class="wordmark"><span class="wordmark-dot"></span>Stonegate Towing</div>
  <p class="services">
    Towing<span class="sep">|</span>Accident towing<span class="sep">|</span>Mechanical breakdown<br>
    Insurance, salvage and recovery<span class="sep">|</span>4wd off road towing<span class="sep">|</span>Light &amp; Heavy towing
  </p>
</section>

<section class="card card-back">
  <div class="wordmark"><span class="wordmark-dot"></span>Stonegate Towing</div>
  <div class="person">
    <div class="person-name">Dana Whitcombe</div>
    <div class="person-role">Owner</div>
  </div>
  <div class="service-badge" role="img" aria-label="24/7 towing service badge"></div>
  <ul class="contacts">
    <li>
      <svg viewBox="0 0 24 24" aria-hidden="true"><path d="M6.6 10.8a15.1 15.1 0 0 0 6.6 6.6l2.2-2.2a1 1 0 0 1 1-.25 11.4 11.4 0 0 0 3.6.57 1 1 0 0 1 1 1V20a1 1 0 0 1-1 1A17 17 0 0 1 3 4a1 1 0 0 1 1-1h3.5a1 1 0 0 1 1 1c0 1.25.2 2.45.57 3.57a1 1 0 0 1-.25 1z"/></svg>
      7354 2618
    </li>
    <li>
      <svg viewBox="0 0 24 24" aria-hidden="true"><path d="M2 5h20v14H2z M2 5l10 8 10-8" stroke="#fff" stroke-width="1.5"/></svg>
      info@stonegatetowing.com.au
    </li>
    <li>
      <svg viewBox="0 0 24 24" aria-hidden="true"><circle cx="12" cy="12" r="10"/><path d="M2 12h20M12 2c3 3 3 17 0 20M12 2c-3 3-3 17 0 20" stroke="#fff" stroke-width="1.3" fill="none"/></svg>
      www.stonegatetowing.com.au
    </li>
  </ul>
</section>

</body>
</html>
```